Website Design for cloud hosting and cloud storage mini site for major UK hosting company

We are a full service managed web hosting company that are setting up a stand alone cloud hosting and cloud storage mini site with a seperate brand name, but predominately stated as the 'cloud hosting arm' of the main company

```html
<!DOCTYPE html>
<html lang="en">
<head>
<meta charset="utf-8">
<title>Stratus Hosting</title>
<link href="https://fonts.googleapis.com/css2?family=Cabin:wght@400;500;700&family=Bungee&display=swap" rel="stylesheet">
<style>
:root{
  --page:#ffffff;
  --ink:#3a3a3a;
  --blue:#2f7fc4;
  --blue-dark:#2466a3;
  --footer:#4a8ccb;
  --footer-base:#3f7dbb;
  --btn-top:#f6fafe;
  --btn-bottom:#d3e4f3;
  --btn-edge:#7ea9cf;
  --field:#c9dcef;
  --field-text:#4a7fb4;
  --rule:#bfbfbf;
  --link-red:#d01f1f;
  --offer-green:#7fc9a5;
  --white:#ffffff;
}
*{box-sizing:border-box;margin:0;padding:0}
html,body{width:1200px;height:1133px;overflow:hidden}
body{background:var(--page);font-family:"Cabin",sans-serif;color:var(--ink);position:relative}
.social-square{position:absolute;width:37px;height:37px;border-radius:5px;background:linear-gradient(#e6e6e6,#b9b9b9);box-shadow:0 2px 3px rgba(0,0,0,.25)}
.brand{position:absolute;left:33px;top:52px;display:flex;align-items:center;gap:14px}
.brand-mark{width:62px;height:70px;border-radius:8px;background:var(--blue)}
.brand-name{font-family:"Cabin",sans-serif;font-weight:700;font-size:66px;color:var(--blue-dark);letter-spacing:-1px;white-space:nowrap}
.btn{position:absolute;height:46px;border:2px solid var(--btn-edge);border-radius:6px;background:linear-gradient(var(--btn-top),var(--btn-bottom));box-shadow:0 2px 3px rgba(0,0,0,.18);display:flex;align-items:center;justify-content:center;font-size:18px;color:#2e5f8e;white-space:nowrap}
.search-field{position:absolute;left:801px;top:183px;width:271px;height:46px;background:var(--field);border:2px solid #9dbfdf;border-radius:3px;padding-left:18px;display:flex;align-items:center;font-size:18px;color:var(--field-text)}
.illus{position:absolute;border-radius:10px}
.intro-title{position:absolute;left:36px;top:306px;font-size:35px;font-weight:400;color:#3f3f3f}
.intro-text{position:absolute;left:36px;top:362px;width:805px;font-size:14.5px;line-height:20px;color:#333}
.intro-text p+p{margin-top:20px}
.rule{position:absolute;height:1px;background:var(--rule)}
.feature h2{position:absolute;font-size:22px;font-weight:400;color:var(--blue);white-space:nowrap}
.feature .thumb{position:absolute;width:80px;height:80px;border-radius:8px;background:linear-gradient(#3a3a3a,#cfd8e0)}
.feature p{position:absolute;width:307px;font-size:14.5px;line-height:20px;text-align:justify;color:#333}
.feature a{position:absolute;font-size:14.5px;color:var(--link-red);text-decoration:underline;white-space:nowrap}
.me-line{position:absolute;left:869px;top:255px;width:296px;height:3px;background:var(--blue)}
.me-badge{position:absolute;left:940px;top:244px;width:155px;height:53px;border-radius:6px;background:linear-gradient(#3fb7d6,#1e86b4);display:flex;align-items:center;gap:10px;padding-left:12px}
.me-badge .avatar{width:36px;height:36px;border-radius:4px;background:#0f6d96}
.me-badge span{font-size:38px;color:var(--white);font-weight:500}
.field{position:absolute;left:869px;width:296px;height:47px;background:var(--field);border:2px solid #9dbfdf;border-radius:3px;padding-left:18px;display:flex;align-items:center;font-size:18px;color:var(--field-text)}
.contact-tile{position:absolute;top:567px;width:70px;text-align:center;font-size:14px;color:var(--blue);white-space:nowrap}
.contact-tile .ico{width:56px;height:52px;margin:0 auto 4px;border-radius:10px}
.phone-bar{position:absolute;left:869px;top:657px;width:296px;height:47px;background:var(--blue);border-radius:4px;color:var(--white);font-size:31px;line-height:1;white-space:nowrap;display:flex;align-items:center;justify-content:space-between;padding:0 10px 0 8px;letter-spacing:.5px}
.phone-bar .go{width:34px;height:26px;border:2px solid var(--white);border-radius:3px;display:flex;align-items:center;justify-content:center;flex:none}
.offer{position:absolute;left:869px;top:728px;width:296px;height:133px;border:2px solid #9dbfdf;border-radius:10px;background:linear-gradient(#ffffff,#eaf2fa)}
.offer-title{position:absolute;left:6px;top:10px;font-family:"Bungee",sans-serif;font-size:25px;line-height:32px;color:var(--offer-green);white-space:nowrap}
.offer-from{position:absolute;left:4px;top:54px;width:50px;height:42px;border-radius:50%;background:#46a7df;color:var(--white);font-size:13px;display:flex;align-items:center;justify-content:center;transform:rotate(-15deg)}
.offer-price{position:absolute;left:22px;top:94px;color:var(--link-red);font-size:28px;line-height:32px;white-space:nowrap}
.offer-price small{font-size:17px}
.cart{position:absolute;left:106px;top:56px;width:150px;height:56px;border:2px solid var(--btn-edge);border-radius:6px;background:linear-gradient(var(--btn-top),var(--btn-bottom));font-size:16px;color:#555;display:flex;align-items:center;padding-left:14px;white-space:nowrap}
.footer{position:absolute;left:0;top:881px;width:1200px;height:252px;background:var(--footer);color:var(--white)}
.footer-col{position:absolute;top:50px;font-size:15px;line-height:20px;white-space:nowrap}
.footer-col h3{font-size:19px;font-weight:700;line-height:22px}
.footer-base{position:absolute;left:0;top:199px;width:1200px;height:53px;background:var(--footer-base);border-top:1px solid #6aa2d6}
.copyright{position:absolute;left:29px;top:15px;font-size:17px;white-space:nowrap}
.partners{position:absolute;left:636px;top:15px;font-size:17px;color:#1d3f66;white-space:nowrap}
.badge{position:absolute;top:10px;height:34px;background:linear-gradient(#f4f4f4,#c8c8c8);border-radius:50%}
.foot-social{position:absolute;top:150px;width:37px;height:37px;border-radius:4px;background:#7fb2e0}
</style>
</head>
<body>

<div class="social-square" style="left:963px;top:3px"></div>
<div class="social-square" style="left:1020px;top:3px"></div>
<div class="social-square" style="left:1077px;top:3px"></div>
<div class="social-square" style="left:1135px;top:3px"></div>

<div class="brand"><div class="brand-mark"></div><div class="brand-name">Stratus Hosting</div></div>

<nav>
  <div class="btn" style="left:36px;top:183px;width:75px">
    <svg width="20" height="18" viewBox="0 0 20 18"><path d="M10 1 L19 9 H16 V17 H12 V12 H8 V17 H4 V9 H1 Z" fill="#2e4f6e"/></svg>
  </div>
  <div class="btn" style="left:129px;top:183px;width:134px">Public Cloud</div>
  <div class="btn" style="left:281px;top:183px;width:135px">Private Cloud</div>
  <div class="btn" style="left:435px;top:183px;width:133px">About Us</div>
  <div class="btn" style="left:587px;top:183px;width:133px">Contact Us</div>
  <div class="search-field">Search</div>
  <div class="btn" style="left:1091px;top:183px;width:74px">
    <svg width="28" height="28" viewBox="0 0 28 28"><circle cx="11" cy="11" r="8" fill="none" stroke="#333" stroke-width="3"/><path d="M17 17 L25 25" stroke="#333" stroke-width="4" stroke-linecap="round"/></svg>
  </div>
</nav>

<div class="illus" role="img" aria-label="Cloud network illustration with connected computers" style="left:664px;top:247px;width:176px;height:116px;background:linear-gradient(135deg,#e8f3fc,#7cc0ee)"></div>

<h1 class="intro-title">Cloud Hosting</h1>
<div class="intro-text">
  <p>DUMMY TEXT----- Cloud VPS hosting, dedicated servers and online back up services are just a few of the many customer-tailored secure hosting products we offer. We use the highest standard enterprise level equipment for our infrastructure and client hardware. All our customers benefit whilst running your mission critical web hosting requirements. All our customers benefit whilst running your mission critical web hosting requirements.</p>
  <p>For robust high performance hosting requirements we offer the latest Veltra technologies within our Dedicated Hosting Server packages.</p>
</div>
<div class="rule" style="left:36px;top:527px;width:805px"></div>

<section class="feature">
  <h2 style="left:55px;top:548px">What is Cloud Hosting</h2>
  <div class="thumb" role="img" aria-label="Server rack on a cloud" style="left:40px;top:587px"></div>
  <p style="left:129px;top:587px">DUMMY TEXT- Cloud VPS hosting, dedicated servers and online back up services are just a few of the many . dummy text.</p>
  <a style="left:348px;top:647px">Read more....</a>

  <h2 style="left:461px;top:553px">Public Cloud</h2>
  <div class="thumb" role="img" aria-label="Server with users on a cloud" style="left:445px;top:587px"></div>
  <p style="left:535px;top:587px">DUMMY TEXT- Cloud VPS hosting, dedicated servers and online back up services are just a few of the many . dummy text.</p>
  <a style="left:754px;top:647px">Read more....</a>

  <h2 style="left:55px;top:701px">Private Cloud</h2>
  <div class="thumb" role="img" aria-label="Locked server on a cloud" style="left:40px;top:745px"></div>
  <p style="left:129px;top:745px">DUMMY TEXT- Cloud VPS hosting, dedicated servers and online back up services are just a few of the many . dummy text.</p>
  <a style="left:348px;top:805px">Read more....</a>

  <h2 style="left:461px;top:701px">About Us</h2>
  <div class="thumb" role="img" aria-label="Doorway on a cloud" style="left:445px;top:745px"></div>
  <p style="left:535px;top:745px">DUMMY TEXT- Cloud VPS hosting, dedicated servers and online back up services are just a few of the many . dummy text.</p>
  <a style="left:754px;top:805px">Read more....</a>
</section>

<aside>
  <div class="me-line"></div>
  <div class="me-badge"><div class="avatar" role="img" aria-label="Account avatar"></div><span>Me!</span></div>
  <div class="field" style="top:324px">Your email</div>
  <div class="field" style="top:401px">Your email</div>
  <div class="btn" style="left:869px;top:477px;width:135px;height:48px">Login</div>
  <div class="btn" style="left:1031px;top:477px;width:134px;height:48px">Subscribe</div>
  <div class="rule" style="left:869px;top:544px;width:296px"></div>

  <div class="contact-tile" style="left:873px;color:#d01f1f"><div class="ico" role="img" aria-label="Live chat icon" style="background:linear-gradient(#a8e05a,#4fa82a)"></div>LiveChat</div>
  <div class="contact-tile" style="left:948px"><div class="ico" role="img" aria-label="Call us icon" style="background:linear-gradient(#bfe3f7,#3a9ad6)"></div>Call Us</div>
  <div class="contact-tile" style="left:1019px"><div class="ico" role="img" aria-label="Mail icon" style="background:linear-gradient(#f2f6fa,#aebfcd)"></div>Mail Us</div>
  <div class="contact-tile" style="left:1096px"><div class="ico" role="img" aria-label="FAQ icon" style="background:linear-gradient(#8fd3f5,#2a8fd0)"></div>FAQ's</div>

  <div class="phone-bar"><span>0800 555 0142</span>
    <div class="go"><svg width="20" height="14" viewBox="0 0 20 14"><path d="M2 2 L8 7 L2 12 M10 2 L16 7 L10 12" fill="none" stroke="#fff" stroke-width="3"/></svg></div>
  </div>

  <div class="offer">
    <div class="offer-title">BEST BUY OFFER</div>
    <div class="offer-from">From</div>
    <div class="offer-price">$99<small>.99</small></div>
    <div class="cart">ADD TO CART
      <svg style="margin-left:8px" width="28" height="24" viewBox="0 0 30 26"><path d="M1 3 H6 L10 17 H25 L28 7 H8" fill="none" stroke="#333" stroke-width="2.5"/><circle cx="12" cy="22" r="2.5" fill="#333"/><circle cx="23" cy="22" r="2.5" fill="#333"/></svg>
    </div>
  </div>
</aside>

<footer class="footer">
  <div class="footer-col" style="left:29px"><h3>HOME</h3>Why choose cloud?<br>Why Altacore?<br>Our infrastructure<br>Testimonials</div>
  <div class="footer-col" style="left:253px"><h3>Public Cloud</h3>Cloud Servers<br>Desktop applications<br>Cloud Hosted Cloud<br>Team Portal</div>
  <div class="footer-col" style="left:456px"><h3>Private Cloud</h3>Why Private Cloud?<br>Private Cloud<br>Desktop applications<br>Cloud Hosted<br>Cloud Portal Mail</div>
  <div class="footer-col" style="left:699px"><h3>About Us</h3>Why Altacore<br>Our infrastructure<br>Knowledge Base<br>Testimonials</div>
  <div class="footer-col" style="left:921px"><h3>Contact Us</h3>Why choose cloud?<br>Company information</div>

  <div class="foot-social" style="left:985px"></div>
  <div class="foot-social" style="left:1042px"></div>
  <div class="foot-social" style="left:1099px"></div>
  <div class="foot-social" style="left:1157px"></div>

  <div class="footer-base">
    <div class="copyright">Copyright 2012. www.stratushosting.co.&nbsp;&nbsp;&nbsp; All Rights reserved</div>
    <div class="partners">Partners &nbsp;|</div>
    <div class="badge" style="left:735px;width:64px;border-radius:4px"></div>
    <div class="badge" style="left:824px;width:42px"></div>
    <div class="badge" style="left:898px;width:34px"></div>
    <div class="badge" style="left:955px;width:40px"></div>
    <div class="badge" style="left:1020px;width:66px"></div>
    <div class="badge" style="left:1117px;width:64px"></div>
  </div>
</footer>

</body>
</html>
```